Elegant Black Candle Label Design!

I need a 2.375" tall by 3.0" wide candle label design. I'm looking for simple and elegant. Black label with silver leaf border and lettering. Label needs to have the following information on it: Fern Hollow Candle Co. as the company name, scent name in the middle and in smaller font, it needs to say Made in USA, All Natural, 8oz. Attached photos are for inspiration.

Target Market(s)

People looking for high end, all natural candle fragrances

Industry/Entity Type

Candle-Spa

Colors

Designer to choose only greyscale colors for use in the design.

Requirements
Must have
• Company Name, Scent (ability to change scent names), All Natural, Made in USA, 8oz
Nice to have
• Black background, silver leaf border and silver leaf font. Elegant fonts maybe slightly cursive

```html
<!DOCTYPE html>
<html lang="en">
<head>
<meta charset="UTF-8">
<title>Fern Hollow Candle Co. — Soy Candle Label</title>
<link rel="stylesheet" href="https://fonts.googleapis.com/css2?family=Poppins:wght@300;400&family=Uncial+Antiqua&display=swap">
<style>
  :root {
    --label-black: #000000;
    --silver: #b4b4b4;
    --silver-light: #cfcfcf;
    --silver-mid: #8a8a8a;
    --silver-dark: #3c3c3c;
    --leaf-shadow: #161616;
  }
  * { margin: 0; padding: 0; box-sizing: border-box; }
  html, body {
    width: 970px;
    height: 1200px;
    overflow: hidden;
    background: var(--label-black);
  }
  .label {
    position: relative;
    width: 970px;
    height: 1200px;
    background: var(--label-black);
    color: var(--silver);
    font-family: "Poppins", sans-serif;
    font-weight: 300;
  }
  .leaf-border {
    position: absolute;
    left: 96px;
    top: 92px;
    width: 780px;
    height: 1016px;
  }
  .brand-mark {
    position: absolute;
    left: 50%;
    top: 262px;
    width: 140px;
    height: 140px;
    margin-left: -70px;
    border: 3px solid var(--silver);
    border-radius: 50%;
  }
  .text-line {
    position: absolute;
    left: 0;
    width: 100%;
    text-align: center;
    line-height: 1;
    white-space: nowrap;
  }
  .brand-name {
    top: 456px;
    font-size: 58px;
    letter-spacing: 0.5px;
    color: var(--silver-light);
  }
  .brand-sub {
    top: 525px;
    font-size: 25px;
    font-weight: 400;
    letter-spacing: 1px;
    color: var(--silver-light);
  }
  .scent-name {
    top: 640px;
    font-family: "Uncial Antiqua", serif;
    font-size: 44px;
    font-weight: 400;
    text-transform: lowercase;
    color: var(--silver);
  }
  .detail {
    font-size: 32px;
    font-weight: 400;
    color: var(--silver);
  }
  .detail-natural { top: 768px; }
  .detail-origin { top: 846px; }
  .detail-weight { top: 922px; }
</style>
</head>
<body>
<main class="label">
  <svg class="leaf-border" viewBox="0 0 780 1016" role="img" aria-label="Silver leaf and berry vine border framing the label">
    <defs>
      <linearGradient id="leafSilver" x1="0" y1="0" x2="1" y2="0">
        <stop offset="0" stop-color="var(--silver-mid)"/>
        <stop offset="0.12" stop-color="var(--silver-dark)"/>
        <stop offset="0.5" stop-color="var(--leaf-shadow)"/>
        <stop offset="0.88" stop-color="var(--silver-dark)"/>
        <stop offset="1" stop-color="var(--silver-mid)"/>
      </linearGradient>
    </defs>
    <path fill="url(#leafSilver)" fill-rule="evenodd"
      d="M0 0H780V1016H0Z M90 92V924H692V92Z"/>
  </svg>

  <div class="brand-mark" aria-hidden="true"></div>
  <p class="text-line brand-name">FERN HOLLOW</p>
  <p class="text-line brand-sub">CANDLE CO</p>

  <h1 class="text-line scent-name">Soy Candle</h1>

  <p class="text-line detail detail-natural">ALL NATURAL</p>
  <p class="text-line detail detail-origin">MADE IN USA</p>
  <p class="text-line detail detail-weight">8oz</p>
</main>
</body>
</html>
```